The Lanternfall Dash 35th Anniversary Poster

Design a poster for the 35th anniversary of The Lanternfall Dash, a 5K with 3,000+ participants that runs through downtown Lexington. The event graphics are heavily influenced by Bertram Holloway's The Copper Orchard Tale. Traditionally the event art keeps the same feel, with slight changes to the color or direction/look of the runners. Original PSD files are available but will not upload to Artvane.

Runners, athletes, active lifestyle

```html
<!DOCTYPE html>
<html lang="en">
<head>
<meta charset="utf-8">
<title>The Lanternfall Dash – 35th Anniversary</title>
<link rel="stylesheet" href="https://fonts.googleapis.com/css2?family=Oswald:wght@300;600;700&family=Parisienne&family=Russo+One&family=Exo+2:ital,wght@1,700;1,800&display=swap">
<style>
  :root {
    --backdrop: #ececec;
    --night-deep: #081a5c;
    --night-mid: #1a3aa8;
    --night-glow: #2f63d8;
    --city-shadow: #0c1f5e;
    --cream: #fbf0c8;
    --gold: #e9cf86;
    --white: #ffffff;
    --ink-blue: #10287a;
    --swoosh: #3d8cf0;
    --rule: #8cc8ff;
  }
  * { margin: 0; padding: 0; box-sizing: border-box; }
  html, body { width: 1198px; height: 1200px; overflow: hidden; background: var(--backdrop); }
  .poster {
    position: absolute; left: 231px; top: 62px; width: 737px; height: 1076px;
    overflow: hidden;
    background: radial-gradient(ellipse at 55% 35%, var(--night-glow) 0%, var(--night-mid) 35%, var(--night-deep) 80%);
  }
  .city-scene {
    position: absolute; left: 0; top: 394px; width: 100%; height: 420px;
    background: linear-gradient(180deg, rgba(12,31,94,0) 0%, var(--city-shadow) 30%, #142e86 75%, rgba(20,46,134,0) 100%);
  }
  .anniversary {
    position: absolute; top: 36px; left: 0; width: 100%; text-align: center;
    font-family: "Oswald", sans-serif; font-weight: 300; font-size: 44px; line-height: 1;
    letter-spacing: 8px; color: var(--white); white-space: nowrap;
  }
  .moon { position: absolute; left: 56px; top: 118px; }
  .title { margin: 0; font-weight: normal; }
  .title-line {
    position: absolute; font-family: "Parisienne", cursive; color: var(--cream);
    line-height: 1; white-space: nowrap;
  }
  .title-top { left: 176px; top: 150px; font-size: 72px; }
  .title-bottom { right: 60px; top: 262px; font-size: 104px; }
  .date-bar {
    position: absolute; left: 186px; top: 436px; width: 380px; height: 80px;
    display: flex; align-items: center; gap: 12px; padding: 0 6px;
  }
  .date-bar::before, .date-bar::after {
    content: ""; position: absolute; left: 0; width: 100%; height: 3px;
    background: linear-gradient(90deg, rgba(120,190,255,0), var(--rule) 25%, var(--rule) 75%, rgba(120,190,255,0));
  }
  .date-bar::before { top: 0; }
  .date-bar::after { bottom: 0; }
  .date-day {
    font-family: "Oswald", sans-serif; font-weight: 600; font-size: 58px; line-height: 1;
    color: var(--white); letter-spacing: -1px; white-space: nowrap;
  }
  .date-divider { width: 3px; height: 44px; background: var(--white); flex: none; }
  .date-when { display: flex; flex-direction: column; line-height: 1; }
  .date-month {
    font-family: "Oswald", sans-serif; font-weight: 600; font-size: 22px;
    color: var(--gold); letter-spacing: 1px; white-space: nowrap;
  }
  .date-year {
    font-family: "Oswald", sans-serif; font-weight: 700; font-size: 34px;
    color: var(--white); letter-spacing: 4px; margin-top: 2px;
  }
  .swooshes { position: absolute; left: 0; top: 800px; }
  .runner-photo {
    position: absolute; left: 446px; top: 595px; width: 258px; height: 440px;
    border-radius: 120px 120px 50px 50px;
    background: linear-gradient(180deg, #2b3f8c 0%, #1b2a6a 60%, #101a44 100%);
  }
  .distance {
    position: absolute; left: 116px; top: 748px;
    font-family: "Russo One", sans-serif; font-size: 176px; line-height: 1;
    transform: skewX(-10deg);
    background: linear-gradient(180deg, #fffbe8 0%, var(--cream) 45%, var(--gold) 100%);
    -webkit-background-clip: text; background-clip: text; color: transparent;
  }
  .participants-box {
    position: absolute; left: 74px; top: 946px; width: 372px; height: 40px;
    background: var(--cream); transform: skewX(-18deg);
    display: flex; align-items: center; justify-content: center;
  }
  .participants-box span {
    transform: skewX(18deg);
    font-family: "Exo 2", sans-serif; font-style: italic; font-weight: 800; font-size: 28px;
    letter-spacing: 6px; color: var(--ink-blue); white-space: nowrap;
  }
  .participants-note {
    position: absolute; left: 74px; top: 994px;
    font-family: "Exo 2", sans-serif; font-style: italic; font-weight: 700; font-size: 30px;
    letter-spacing: 2px; color: var(--white); white-space: nowrap;
  }
</style>
</head>
<body>
<main class="poster">
  <div class="city-scene" role="img" aria-label="Night view of a downtown street with a domed courthouse, lit in deep blue"></div>

  <p class="anniversary">35TH ANNIVERSARY</p>

  <svg class="moon" width="230" height="230" viewBox="0 0 230 230" aria-hidden="true">
    <path d="M115 5 A112 112 0 1 0 225 190 A95 95 0 1 1 115 5 Z" fill="var(--white)"/>
  </svg>

  <h1 class="title">
    <span class="title-line title-top">The Lanternfall</span>
    <span class="title-line title-bottom">Dash</span>
  </h1>

  <div class="date-bar">
    <span class="date-day">SATURDAY</span>
    <span class="date-divider"></span>
    <span class="date-when">
      <span class="date-month">AUGUST 11</span>
      <span class="date-year">2019</span>
    </span>
  </div>

  <svg class="swooshes" width="737" height="276" viewBox="0 0 737 276" aria-hidden="true">
    <path d="M0 120 Q360 290 737 60" fill="none" stroke="var(--swoosh)" stroke-width="3" opacity="0.7"/>
    <path d="M0 150 Q360 310 737 90" fill="none" stroke="var(--swoosh)" stroke-width="2" opacity="0.5"/>
    <path d="M0 195 Q380 320 737 150 L737 276 L0 276 Z" fill="#0f2fa0" opacity="0.8"/>
    <path d="M0 235 Q400 330 737 205" fill="none" stroke="#5aa8ff" stroke-width="3" opacity="0.6"/>
  </svg>

  <div class="runner-photo" role="img" aria-label="Sprinter in a blue vest running forward"></div>

  <p class="distance">5K</p>
  <div class="participants-box"><span>WITH 3,000</span></div>
  <p class="participants-note">+PARTICIPANTS RUNS</p>
</main>
</body>
</html>
```